Website Design Required For Education Video Portfolio Site

I am looking for a designer to create a skin for a relaunch of my website - www.brightfieldlearningfilms.co.uk. We want a clean and stylish new design.

The website showcases prospectus/promotional videos that are made for schools and colleges. Videos will be hosted on YouTube and embedded.

I want it to be stylish and clean.

I require 7 pages designed and this must be agreed in order to do the project.

1. Homepage
2. About
3. Prices
4. Testimonials
5. Contact Page with form
6. Promotional Videos
7. Subject Videos

The website will be then be built on the Wordpress system.

Target Market(s)

Education, Schools, Colleges, Universities

Industry/Entity Type

Education

Font styles to use
Serif

Colors

Designer to choose colors to be used in the design.

Requirements
Must have
• Video content, be clean, show our portfolio, descriptions about videos. I like the idea of having video headers.
Nice to have
• Images

```html
<!DOCTYPE html>
<html lang="en">
<head>
<meta charset="utf-8">
<title>Brightfield Learning Films — Home</title>
<link rel="stylesheet" href="https://fonts.googleapis.com/css2?family=Montserrat:wght@500;700;800&family=Nunito+Sans:wght@300;400;600;700&family=Roboto+Slab:wght@400&display=swap">
<style>
:root{
  --blue:#1ba7e3;
  --blue-dark:#2a64b4;
  --ink:#111111;
  --text:#3d3d3d;
  --muted:#5e5e5e;
  --rule:#e2e2e2;
  --white:#ffffff;
}
*{box-sizing:border-box;margin:0;padding:0}
html,body{width:1200px;height:4405px;overflow:hidden;background:var(--white)}
body{position:relative;font-family:"Nunito Sans",sans-serif;color:var(--text)}
.abs{position:absolute}
.brand{display:flex;align-items:center;gap:8px;font-family:"Montserrat",sans-serif;font-weight:800;color:var(--blue)}
.brand-mark{background:var(--blue);border-radius:6px}
.nav{position:absolute;top:0;left:0;width:1200px;height:96px}
.nav .brand{position:absolute;left:133px;top:28px;font-size:26px}
.nav .brand-mark{width:34px;height:34px}
.nav ul{position:absolute;right:133px;top:40px;display:flex;gap:27px;list-style:none;font-family:"Montserrat",sans-serif;font-size:12.5px;font-weight:500;color:#222}
.nav li.active{color:var(--blue)}
.photo{position:absolute}
.play{position:absolute;border-radius:50%}
.hero{left:0;top:96px;width:1200px;height:570px;background:linear-gradient(160deg,#6d7a4c 0%,#4d5a3a 40%,#7a5060 60%,#3f4a30 100%)}
.hero-title{position:absolute;top:414px;left:0;width:1200px;text-align:center;font-family:"Montserrat",sans-serif;font-weight:800;font-size:44px;line-height:52px;color:var(--white);text-shadow:0 2px 6px rgba(0,0,0,.4)}
.feature-caption{position:absolute;top:998px;width:270px;text-align:center;font-size:13px;line-height:19.5px;color:var(--muted);font-weight:300}
.h2{font-family:"Montserrat",sans-serif;font-weight:700;color:var(--ink);text-transform:uppercase}
.center{text-align:center}
.body-copy{font-size:12.5px;line-height:19.5px;color:var(--muted)}
.underline{position:absolute;height:2px;width:88px;background:var(--blue-dark)}
.btn{position:absolute;background:var(--blue);color:var(--white);font-family:"Montserrat",sans-serif;font-weight:700;font-size:10.5px;display:flex;align-items:center;justify-content:center;letter-spacing:.3px}
.quote{position:absolute;left:137px;top:1328px;width:921px;height:432px;background:linear-gradient(170deg,#8b8d84 0%,#6f7466 45%,#5d6a52 100%)}
.quote-text{position:absolute;left:0;top:120px;width:921px;text-align:center;font-family:"Roboto Slab",serif;font-size:46px;line-height:63px;color:#f3f3f3;text-shadow:0 2px 4px rgba(0,0,0,.5)}
.quote-cite{position:absolute;left:0;top:330px;width:921px;text-align:center;font-family:"Roboto Slab",serif;font-size:24px;line-height:36px;color:#e6e6e6;text-shadow:0 2px 4px rgba(0,0,0,.5)}
.partner{position:absolute;border-radius:50%}
.drone{left:0;top:3750px;width:1200px;height:400px;background:linear-gradient(180deg,#2c3a22 0%,#4b5a3b 50%,#2a3520 100%)}
.drone-kicker{position:absolute;top:3893px;width:1200px;text-align:center;color:#fff;font-size:19px;font-weight:400}
.drone-title{position:absolute;top:3932px;width:1200px;text-align:center;color:#fff;font-family:"Montserrat",sans-serif;font-weight:700;font-size:23px;line-height:33px}
.footer-head{font-family:"Montserrat",sans-serif;font-weight:700;font-size:18px;color:var(--blue)}
.footer-copy{font-size:14px;line-height:19px;color:#222;margin-top:4px}
.legal{position:absolute;top:4328px;width:1200px;text-align:center;font-size:10.5px;line-height:19px;color:#444}
</style>
</head>
<body>

<header class="nav">
  <div class="brand"><span class="brand-mark"></span>Brightfield</div>
  <ul>
    <li class="active">HOME</li><li>ABOUT</li><li>PROMOTIONAL VIDEOS</li><li>SUBJECT VIDEOS</li><li>PRICES</li><li>TESTIMONIALS</li><li>CONTACT</li>
  </ul>
</header>

<section class="photo hero" role="img" aria-label="Video header: young pupils in school uniform playing at an outdoor mud kitchen in a school garden"></section>
<svg class="abs" style="left:573px;top:331px" width="54" height="54" viewBox="0 0 54 54" aria-hidden="true"><circle cx="27" cy="27" r="24" fill="none" stroke="#fff" stroke-width="3"/><path d="M21 16 L38 27 L21 38 Z" fill="#fff"/></svg>
<h1 class="hero-title">WE MAKE AWESOME<br>EDUCATIONAL VIDEO</h1>

<div class="photo" style="left:133px;top:714px;width:297px;height:257px;background:linear-gradient(160deg,#8b6a45,#5d7fa8 60%,#3d5f88)" role="img" aria-label="Boy climbing on playground rope equipment"></div>
<div class="photo" style="left:453px;top:714px;width:297px;height:257px;background:linear-gradient(160deg,#e9e7e4,#cfc9c2 60%,#b7a99b)" role="img" aria-label="Children playing with building blocks on a carpet"></div>
<div class="photo" style="left:768px;top:714px;width:297px;height:257px;background:linear-gradient(160deg,#c4b05a,#6f9a3c 55%,#4f7f2b)" role="img" aria-label="Group of children running across a sunny field"></div>
<p class="feature-caption" style="left:146px">We're a smart bunch of experienced video makers and we know how to create compelling videos that get results.</p>
<p class="feature-caption" style="left:466px">We offer a cost-effective marketing solution – no more expensive brochure designing, printing and storage hassles. A video beats traditional marketing materials hands down.</p>
<p class="feature-caption" style="left:781px">We save you time and effort – you could invest time, effort and tech into making your own videos, but would they have the same polished, professional impact as ours?</p>

<h2 class="h2 center abs" style="top:1148px;width:1200px;font-size:24.5px;line-height:35px">Creating bespoke education videos to showcase schools,<br>colleges &amp; training providers in the north of England</h2>
<p class="body-copy center abs" style="left:170px;top:1238px;width:860px">Here at Brightfield Learning Films, we know how to create stylish, engaging, and successful educational videos for schools, colleges and training providers. We've been making them for years.  We believe that when you're trying to attract new learners the best way to show how your learning establishment is better than the rest is with a compelling, top-quality video.</p>

<section class="quote" role="img" aria-label="Video testimonial: aerial view of a primary school and surrounding streets">
  <span class="abs" style="left:36px;top:16px;width:62px;height:62px;border-radius:50%;background:#f4f1e8"></span>
  <p class="quote-text">Within 6 weeks of the video<br>being launched we had<br>4 children start our school.</p>
  <p class="quote-cite">Clara Henshaw<br>Larkmoor Primary School, Ashbrook</p>
</section>
<svg class="abs" style="left:580px;top:1513px" width="40" height="40" viewBox="0 0 40 40" aria-hidden="true"><circle cx="20" cy="20" r="20" fill="var(--blue)"/><path d="M16 12 L28 20 L16 28 Z" fill="#fff"/></svg>

<div class="photo" style="left:133px;top:1836px;width:489px;height:390px;background:linear-gradient(160deg,#e6ecea,#bcd3cd 50%,#8fa7a0)" role="img" aria-label="Excited children running down a bright school corridor"></div>
<h2 class="h2 abs" style="left:675px;top:1848px;font-size:23px;line-height:32px">A one-off investment that<br>brings long-term results</h2>
<span class="underline" style="left:675px;top:1924px"></span>
<div class="body-copy abs" style="left:675px;top:1950px;width:395px">
  <p>There are so many ways to repurpose your videos and make the initial investment work for you – sharing snippets on social media, embedding the video onto your website, uploading it to your video channel or playing it on your welcome screen in reception. The return on investment is excellent (and in some cases, instant!)</p>
  <p style="margin-top:19px">BY THE WAY: don't just take our word for how successful our videos are. Check out some of the wonderful feedback we've received.</p>
</div>
<div class="btn" style="left:675px;top:2169px;width:174px;height:39px">READ OUR FEEDBACK</div>

<h2 class="h2 abs" style="left:133px;top:2318px;font-size:23px;line-height:32px">Our videos won't eat up<br>all of your marketing<br>budget either!</h2>
<span class="underline" style="left:133px;top:2428px"></span>
<p class="body-copy abs" style="left:133px;top:2458px;width:290px">You see we do things differently at Brightfield Learning Films. Our highly experienced and dedicated team is small (but mighty) and that's how we keep costs low and affordable.</p>
<div class="btn" style="left:133px;top:2583px;width:150px;height:38px">VIEW OUR PRICES</div>
<div class="photo" style="left:578px;top:2305px;width:489px;height:332px;background:linear-gradient(160deg,#6b4a2e,#a06a3c 45%,#3d2a1d)" role="img" aria-label="Laughing children playing drums in a music lesson"></div>

<h2 class="h2 center abs" style="top:2728px;width:1200px;font-size:23px;line-height:32px">Creating customised educational videos<br>that exceed your expectations</h2>
<span class="underline" style="left:556px;top:2811px"></span>
<p class="body-copy center abs" style="left:230px;top:2842px;width:740px">Prefer a prospectus video over a music-driven one? No problem. In fact, we can almost always cater for your specific needs and budgets. All you have to do is ask. Our mission is to capture the heart and soul of your school, college, training company, so your potential recruits can't resist taking that next step towards enrolling. Take a look at our range of video offerings https://brightfieldlearningfilms.co.uk/our-work/.</p>

<div class="photo" style="left:133px;top:2957px;width:300px;height:229px;background:linear-gradient(160deg,#b9b4a8,#5b5a6e 60%,#2d2f4a)" role="img" aria-label="Video thumbnail: two pupils at a school main entrance"></div>
<div class="photo" style="left:450px;top:2957px;width:300px;height:229px;background:linear-gradient(160deg,#7d8480,#55604a 55%,#3a4535)" role="img" aria-label="Video thumbnail: aerial view of school buildings"></div>
<div class="photo" style="left:768px;top:2957px;width:300px;height:229px;background:linear-gradient(160deg,#8fa6c0,#b39a52 45%,#3e6a3a)" role="img" aria-label="Video thumbnail: pupil on playground climbing frame"></div>
<svg class="abs" style="left:250px;top:3051px" width="42" height="42" viewBox="0 0 40 40" aria-hidden="true"><circle cx="20" cy="20" r="20" fill="var(--blue)"/><path d="M16 12 L28 20 L16 28 Z" fill="#fff"/></svg>
<svg class="abs" style="left:579px;top:3051px" width="42" height="42" viewBox="0 0 40 40" aria-hidden="true"><circle cx="20" cy="20" r="20" fill="var(--blue)"/><path d="M16 12 L28 20 L16 28 Z" fill="#fff"/></svg>
<svg class="abs" style="left:897px;top:3051px" width="42" height="42" viewBox="0 0 40 40" aria-hidden="true"><circle cx="20" cy="20" r="20" fill="var(--blue)"/><path d="M16 12 L28 20 L16 28 Z" fill="#fff"/></svg>
<div class="btn" style="left:527px;top:3221px;width:150px;height:39px">WATCH OUR VIDEOS</div>

<h2 class="h2 center abs" style="top:3320px;width:1200px;font-size:23px;line-height:32px">Schools, colleges and training<br>providers we've worked with</h2>
<span class="underline" style="left:556px;top:3401px"></span>
<span class="partner" style="left:150px;top:3450px;width:90px;height:90px;background:#e8e4f0"></span>
<span class="partner" style="left:355px;top:3450px;width:90px;height:90px;background:#e3efd2"></span>
<span class="partner" style="left:555px;top:3450px;width:90px;height:90px;background:#eeeeee"></span>
<span class="partner" style="left:757px;top:3450px;width:90px;height:90px;background:#d9ebdc"></span>
<span class="partner" style="left:955px;top:3472px;width:96px;height:48px;border-radius:0;background:#6b3a70"></span>
<span class="partner" style="left:163px;top:3605px;width:90px;height:90px;background:#d8eddf"></span>
<span class="partner" style="left:355px;top:3605px;width:90px;height:90px;background:#f6e0d6"></span>
<span class="partner" style="left:548px;top:3605px;width:90px;height:90px;background:#e1f1f4"></span>
<span class="partner" style="left:738px;top:3605px;width:90px;height:90px;background:#e1e6f5"></span>
<span class="partner" style="left:938px;top:3605px;width:90px;height:90px;background:#1e5aa8"></span>

<section class="photo drone" role="img" aria-label="Children running through woodland, darkened behind text"></section>
<p class="drone-kicker">LICENSED BY THE NATIONAL AIR SAFETY BOARD</p>
<h2 class="drone-title">WE ARE LICENSED DRONE OPERATORS<br>MEANING WE CAN TAKE TO THE SKY.</h2>

<footer>
  <div class="brand abs" style="left:133px;top:4160px;font-size:38px"><span class="brand-mark" style="width:50px;height:50px"></span>Brightfield</div>
  <div class="abs" style="left:480px;top:4160px;width:240px">
    <h3 class="footer-head">OUR MISSION</h3>
    <p class="footer-copy">Striving to deliver quality video content for schools and colleges in the North of England.</p>
  </div>
  <div class="abs" style="left:822px;top:4160px;width:300px">
    <h3 class="footer-head">CONTACT US</h3>
    <p class="footer-copy">07700 900 318<br>hello@brightfieldlearningfilms.co.uk</p>
  </div>
  <span class="abs" style="left:133px;top:4300px;width:934px;height:1px;background:var(--rule)"></span>
  <p class="legal">© Brightfield Learning Films Limited 2023. All Rights Reserved.<br>Company Registration Number: 10482716.</p>
</footer>

</body>
</html>
```